Broschüre für Anbieter von Hundespielzeug und -snacks
Zielgruppe
wir werden einen Onlineshop eröffnen für enrichment Hundespielzeug und gesunde snacks. Das ganze ist seine based und in unserer dog daycare täglich getestet von echten Hunden.
Aufgabenstellung
es sollte alles in einem seine based lab design mit den Farben Blau, weiss, hellgrau gehalten werden. eventuell noch gelb und rot. ich liefere alle Texte.

```html
<!DOCTYPE html>
<html lang="en">
<head>
<meta charset="utf-8">
<title>Tails &amp; Treats – Enrichment Lab Cookbook</title>
<link href="https://fonts.googleapis.com/css2?family=Quicksand:wght@400;500;600;700&display=swap" rel="stylesheet">
<style>
  :root{
    --teal:#1597b0;
    --navy:#0d3f5c;
    --ink:#1f6482;
    --sky:#96c3d3;
    --pale:#dfeaf1;
    --yellow:#efd04f;
    --red:#b11b28;
    --text:#25323b;
    --white:#ffffff;
  }
  *{box-sizing:border-box;margin:0;padding:0}
  html,body{width:846px;height:1200px;overflow:hidden;background:var(--white)}
  body{position:relative;font-family:"Quicksand",sans-serif;color:var(--ink)}
  .page{position:absolute;width:242px;height:242px;background:var(--white);overflow:hidden;box-shadow:0 2px 6px rgba(0,0,0,.12)}
  .page > svg.bg{position:absolute;inset:0;width:100%;height:100%}
  .abs{position:absolute}
  .paw{width:18px;height:18px;fill:var(--teal)}
  .tube{position:absolute;background:var(--navy);border-radius:6px 6px 8px 8px}

  /* cover */
  .cover{left:107px;top:40px;width:307px;height:307px;transform:rotate(-8deg);background:var(--sky)}
  .cover .brand-top{left:0;right:0;top:76px;text-align:center;transform:translateX(10px);font-weight:700;font-size:10.5px;color:var(--navy);letter-spacing:.3px;line-height:1.1}
  .cover .brand-top small{display:block;font-size:4px;letter-spacing:2px;font-weight:500}
  .cover .title{left:40px;top:118px;width:240px;text-align:center;color:var(--white);font-weight:700;line-height:1.3}
  .cover .title .t1{font-size:11.5px;display:block}
  .cover .title .t2{font-size:16px;display:block;letter-spacing:.3px}
  .cover .photo{left:115px;top:165px;width:180px;height:120px;border-radius:50%;background:radial-gradient(ellipse at 60% 55%,#b8705a 0%,#d9c6bc 35%,#f3f1ee 70%)}
  .cover .mark{left:40px;top:250px;display:flex;align-items:center;gap:5px;color:var(--navy);font-weight:700;font-size:9px;line-height:1.2}
  .cover .mark i{width:14px;height:14px;border-radius:50%;background:var(--navy);display:block}
  .cover .mark small{display:block;font-size:5px;font-weight:500}

  /* welcome */
  .welcome{left:408px;top:32px;width:292px;height:291px}
  .welcome h2{left:65px;top:66px;font-size:10px;font-weight:700;color:var(--navy);letter-spacing:.2px}
  .welcome .copy{left:30px;top:88px;width:250px;font-size:8px;line-height:10.5px;color:var(--ink)}
  .welcome .copy b{color:var(--navy);font-weight:700}
  .welcome .copy p+p{margin-top:10px}

  /* protocols */
  .centered{left:14px;right:14px;text-align:center;font-size:6.6px;line-height:8.7px;color:var(--ink)}
  .red{color:var(--red);font-weight:700;display:block}
  .heading-red{color:var(--red);font-weight:700;font-size:8.4px}

  /* formulas */
  .formula h2{font-size:9px;font-weight:600;color:var(--navy);letter-spacing:.2px}
  .objective{text-align:center;font-size:6.7px;line-height:8.7px;color:var(--ink)}
  .objective u{font-weight:700;color:var(--navy)}
  .pill{position:absolute;left:0;height:19px;background:var(--yellow);border-radius:0 10px 10px 0;color:var(--white);font-size:7.4px;font-weight:600;display:flex;align-items:center;padding-left:20px}
  .ingr{position:absolute;font-size:6.6px;line-height:8.8px;color:var(--text)}
  .ingr b{font-weight:700;display:block}
  .ingr li{list-style:none}
  .ingr li::before{content:"• "}

  /* notes */
  .notes{left:51px;top:929px;width:204px;height:204px;transform:rotate(-15deg)}
  .notes h2{left:20px;top:48px;font-size:9.5px;font-weight:700;color:var(--navy);letter-spacing:.3px}
</style>
</head>
<body>
<svg width="0" height="0" style="position:absolute">
  <symbol id="paw" viewBox="0 0 24 24">
    <ellipse cx="13" cy="16" rx="6.5" ry="5.5"/>
    <circle cx="5" cy="10" r="2.5"/><circle cx="9" cy="5" r="2.6"/>
    <circle cx="15" cy="4.5" r="2.6"/><circle cx="20" cy="9" r="2.5"/>
  </symbol>
</svg>

<!-- Cover -->
<section class="page cover">
  <svg class="bg" viewBox="0 0 300 300" preserveAspectRatio="none">
    <path d="M0 135 C70 85 150 120 200 55 C215 35 222 15 225 0 L300 0 L300 240 C230 225 140 225 80 235 L0 240 Z" fill="var(--teal)"/>
    <path d="M0 140 C70 90 150 125 205 60 C220 40 228 18 231 0" fill="none" stroke="var(--navy)" stroke-width="5"/>
  </svg>
  <div class="abs brand-top">TAILS &amp; TREATS<small>DOG ENRICHMENT LAB</small></div>
  <div class="abs title"><span class="t1">THE TAILS &amp; TREATS</span><span class="t2">ENRICHMENT LAB COOKBOOK</span></div>
  <div class="abs photo" role="img" aria-label="Photo of a dog licking a blue bowl of fresh raw food"></div>
  <svg class="abs paw" style="left:258px;top:255px;fill:var(--white)"><use href="#paw"/></svg>
  <div class="abs mark"><i></i><span>Tails &amp; Treats<small>Enrichment tested every day</small></span></div>
</section>

<!-- Welcome -->
<section class="page welcome">
  <svg class="bg" viewBox="0 0 292 291" preserveAspectRatio="none">
    <path d="M0 0 L185 0 C195 30 180 50 130 52 C70 55 20 70 0 100 Z" fill="var(--teal)"/>
    <path d="M160 0 C175 25 165 40 120 44" fill="none" stroke="var(--navy)" stroke-width="5"/>
    <path d="M20 275 C100 285 160 200 230 205 C260 207 280 215 292 220 L292 291 L25 291 Z" fill="var(--pale)"/>
    <path d="M20 275 C100 285 160 200 230 205 C260 207 280 215 292 222" fill="none" stroke="var(--teal)" stroke-width="1"/>
  </svg>
  <h2 class="abs">WELCOME TO THE LAB</h2>
  <svg class="abs paw" style="left:184px;top:61px"><use href="#paw"/></svg>
  <div class="abs copy">
    <p><b>Congratulations,</b><br>you are now a certified Tails &amp; Treats Lab Technician.<br>You hold in your hands the official cookbook,<br>the result of extensive research into canine enrichment<br>and mental well-being. This is not just food;<br>&nbsp;&nbsp;&nbsp;&nbsp;&nbsp;&nbsp;&nbsp;&nbsp;&nbsp;&nbsp;&nbsp;it's a tool for behavioral optimization.</p>
    <p><b>Your mission:</b><br>Synthesis these potent formulas and deploy them<br>via the specialized enrichment devices (toys)<br>included in your box<br>to unlock your dog's potential.</p>
  </div>
  <svg class="abs paw" style="left:150px;top:228px;width:38px;height:38px"><use href="#paw"/></svg>
  <div class="tube" style="left:215px;top:214px;width:14px;height:62px" role="img" aria-label="Bone-topped test tube illustration"></div>
</section>

<!-- Protocols spread -->
<section class="page" style="left:198px;top:376px">
  <svg class="bg" viewBox="0 0 242 242" preserveAspectRatio="none">
    <path d="M0 0 L242 0 L242 40 C180 55 60 55 0 35 Z" fill="var(--pale)"/>
  </svg>
  <div class="abs centered" style="top:28px"><span class="heading-red">IMPORTANT LABORATORY PROTOCOLS</span><br>(PLEASE READ)</div>
  <div class="abs centered" style="top:64px">Before initiating synthesis,<br>review these critical safety directives:</div>
  <svg class="abs paw" style="left:112px;top:90px"><use href="#paw"/></svg>
  <div class="abs centered" style="top:112px"><span class="red">SAFETY FIRST:</span>Ensure ALL ingredients are 100% dog-safe.<br>NEVER use xylitol (a common sweetener in peanut butter),<br>grapes, raisins, onions, garlic, chocolate or macadamia nuts.</div>
  <svg class="abs paw" style="left:112px;top:150px"><use href="#paw"/></svg>
  <div class="abs centered" style="top:172px"><span class="red">TECHNICIAN DISCRETION:</span>Always consult your veterinarian before introducing<br>new foods or supplements, especially for dogs with<br>existing health conditions or known allergies.</div>
</section>
<section class="page" style="left:440px;top:376px">
  <svg class="bg" viewBox="0 0 242 242" preserveAspectRatio="none">
    <path d="M0 120 C30 140 50 200 100 210 C150 220 200 200 242 215 L242 242 L0 242 Z" fill="var(--pale)"/>
    <path d="M0 145 C30 160 50 210 100 212 C150 214 200 205 242 222" fill="none" stroke="var(--teal)" stroke-width="4"/>
  </svg>
  <svg class="abs paw" style="left:112px;top:34px"><use href="#paw"/></svg>
  <div class="abs centered" style="top:56px"><span class="red">THE "WORK" PHASE:</span>The secret is in the temperature.<br>Freezing a loaded enrichment device dramatically<br>increases the "work" required,<br>providing a superior cognitive challenge.</div>
  <svg class="abs paw" style="left:112px;top:105px"><use href="#paw"/></svg>
  <div class="abs centered" style="top:126px"><span class="red">CALORIE CALIBRATION:</span>Adjust your dog's main meal portions<br>to account for the calories<br>synthesized in these enrichment formulas.<br>Over-calibration is a lab violation.</div>
</section>

<!-- Formula P spread -->
<section class="page formula" style="left:255px;top:645px">
  <svg class="bg" viewBox="0 0 242 242" preserveAspectRatio="none">
    <path d="M0 0 L242 0 L242 110 C225 90 215 40 175 45 C120 50 50 55 0 40 Z" fill="var(--pale)"/>
    <path d="M0 185 C30 205 50 225 120 225 C180 225 215 215 242 224" fill="none" stroke="var(--teal)" stroke-width="4"/>
  </svg>
  <h2 class="abs" style="left:55px;top:24px">FORMULA P | DEVELOPMENT</h2>
  <svg class="abs paw" style="left:188px;top:34px;width:22px;height:22px"><use href="#paw"/></svg>
  <div class="abs objective" style="left:30px;width:200px;top:57px"><u>Primary Objective</u>:<br>Accelerated Cognitive Growth &amp; Optimized<br>Teething Relief the "Neuron-Nutrient-Booster" –<br>engineered for growing brain matter<br>and achy, developing jaws.</div>
  <div class="pill" style="top:110px;width:148px">SYNT-1. "Puppy Brain Builder"</div>
  <ul class="ingr" style="left:21px;top:139px"><b>Ingredients:</b>
    <li>100g Cooked Sweet Potato (mashed, no skins)</li>
    <li>1 tbsp Salmon Oil (critical for Omega-3 fatty acid infusion)</li>
    <li>5-6 Blueberries (antioxidant deployment)</li>
    <li>A few soaked rolled oats (for texture variable)</li>
  </ul>
  <div class="tube" style="left:193px;top:175px;width:10px;height:38px" role="img" aria-label="Test tube icon"></div>
</section>
<section class="page formula" style="left:502px;top:645px">
  <svg class="bg" viewBox="0 0 242 242" preserveAspectRatio="none">
    <path d="M242 0 L215 0 C195 40 195 120 210 170 C220 210 150 220 120 242 L242 242 Z" fill="var(--pale)"/>
  </svg>
  <div class="pill" style="top:22px;width:156px">SYNT-2. "Teething Relief Puree"</div>
  <ul class="ingr" style="left:21px;top:51px"><b>Ingredients:</b>
    <li>100g Plain Greek Yogurt (low-fat, unsweetened)</li>
    <li>1 tbsp Pumpkin Puree (pure canned pumpkin, NOT pie filling)</li>
    <li>1 tsp Coconut Oil (melted and cooled)</li>
  </ul>
  <div class="pill" style="top:93px;width:156px">SYNT-3. "The Forager" Dry Mix</div>
  <ul class="ingr" style="left:21px;top:122px"><b>Ingredients:</b>
    <li>Handful of freeze-dried beef or lamb liver (crumbled)</li>
    <li>Handful of air-dried sweet potato chips (crumbled)</li>
    <li>A few high-quality, small-breed puppy kibble pieces</li>
  </ul>
  <div class="pill" style="top:165px;width:156px">SYNT-4. "Brainy Bites" Challenge</div>
  <ul class="ingr" style="left:21px;top:193px"><b>Ingredients:</b>
    <li>Handful of small, grain-free puppy treats</li>
    <li>A few raw baby carrot sticks (halved)</li>
  </ul>
</section>

<!-- Lab notes -->
<section class="page notes">
  <svg class="bg" viewBox="0 0 204 204" preserveAspectRatio="none">
    <path d="M0 0 L204 0 L204 22 C150 20 140 90 60 95 C30 97 10 96 0 95 Z" fill="var(--pale)"/>
    <path d="M0 95 C60 100 120 85 150 45 C170 25 190 22 204 22" fill="none" stroke="var(--teal)" stroke-width="1"/>
    <g stroke="var(--sky)" stroke-width="1" stroke-dasharray="4 3">
      <line x1="10" y1="110" x2="194" y2="110"/><line x1="10" y1="128" x2="194" y2="128"/>
      <line x1="10" y1="146" x2="194" y2="146"/><line x1="10" y1="164" x2="194" y2="164"/>
      <line x1="10" y1="182" x2="194" y2="182"/><line x1="10" y1="198" x2="194" y2="198"/>
      <line x1="60" y1="92" x2="194" y2="92"/><line x1="120" y1="74" x2="194" y2="74"/>
    </g>
  </svg>
  <h2 class="abs">LAB NOTES</h2>
  <svg class="abs paw" style="left:140px;top:38px"><use href="#paw"/></svg>
</section>

<!-- Formula E spread -->
<section class="page formula" style="left:325px;top:914px">
  <svg class="bg" viewBox="0 0 242 242" preserveAspectRatio="none">
    <path d="M0 0 L242 0 L242 115 C225 95 215 45 175 48 C120 52 50 58 0 42 Z" fill="var(--pale)"/>
    <path d="M0 185 C30 205 50 225 120 225 C180 225 215 215 242 224" fill="none" stroke="var(--teal)" stroke-width="4"/>
  </svg>
  <h2 class="abs" style="left:59px;top:26px">FORMULA E | CALIBRATION</h2>
  <svg class="abs paw" style="left:185px;top:36px;width:22px;height:22px"><use href="#paw"/></svg>
  <div class="abs objective" style="left:25px;width:200px;top:64px"><u>Primary Objective:</u><br>Energy Conversion &amp; Restless Behavior Mitigation<br>The "Centering-Blend" –<br>designed to convert high-frequency chaotic energy<br>into focused, constructive activity.</div>
  <div class="pill" style="top:117px;width:182px">SYNT-1. "Focused Work" Chicken Salad</div>
  <ul class="ingr" style="left:25px;top:146px"><b>Ingredients:</b>
    <li>100g Lean, Cooked Chicken Breast (finely shredded)</li>
    <li>1 tbsp Cottage Cheese (low-fat, plain)</li>
    <li>1 tsp Chia Seeds (must be soaked in 1 tbsp of water<br>&nbsp;&nbsp;for 15 mins to form a gel)</li>
    <li>A few green beans (finely chopped)</li>
  </ul>
</section>
<section class="page formula" style="left:571px;top:914px">
  <svg class="bg" viewBox="0 0 242 242" preserveAspectRatio="none">
    <path d="M242 0 L215 0 C195 40 195 120 210 170 C220 210 150 220 120 242 L242 242 Z" fill="var(--pale)"/>
  </svg>
  <div class="pill" style="top:25px;width:158px">SYNT-2. "Sardine Calibration Crew"</div>
  <ul class="ingr" style="left:22px;top:54px"><b>Ingredients:</b>
    <li>100g Pure Peanut Butter (XYLITOL-FREE! Check the label)</li>
    <li>Canned Sardines in WATER (drained and mashed)</li>
    <li>1 tsp Flaxseed Oil</li>
  </ul>
  <div class="pill" style="top:96px;width:158px">SYNT-3. Mixed Texture Calibration</div>
  <ul class="ingr" style="left:22px;top:125px"><b>Ingredients:</b>
    <li>Handful of dry kibble</li>
    <li>Handful of dehydrated beef lung cubes</li>
    <li>A few small dollops of unsweetened applesauce</li>
  </ul>
  <div class="pill" style="top:168px;width:158px">SYNT-4. High-Fiber Energy Crunch</div>
  <ul class="ingr" style="left:22px;top:197px"><b>Ingredients:</b>
    <li>Handful of air-popped popcorn (no salt or butter)</li>
    <li>Handful of high-fiber dry kibble</li>
  </ul>
</section>
</body>
</html>
```